Erotic romance novelist requires book cover design for new trilogy

I have written a trilogy of erotic romance novels about a young woman and two young men at a northern university, who begin a house share as strangers. The girl is attracted to both men and vice versa. The house is sometimes claustrophobic as the men vie for her attentions and she ultimately chooses neither, thus a delicate menage à trois develops. In the later books of the trilogy, a slowly developing intimate relationship between the two men is explored further and the love and friendship between the three of them is cemented. The chosen design will set the atmosphere for the remaining two book covers in the trilogy. I would like it to be delicately oblique and suggestive.

Target Market(s)

young adults and women aged 18-50

Font styles to use
Decorative
Script

Colors

Designer to choose colors to be used in the design.

Requirements
Must have
• The trilogy is called Hartwell Vale and book 1 is called Falling Softly
• I would like a subtle reference to the 'trhreesome' nature of the story
Nice to have
• The female student is studying art history and has an interest in greek sculpture - I have added an inspirational photo

```html
<!DOCTYPE html>
<html lang="en">
<head>
<meta charset="utf-8">
<title>Falling Softly — Maren Ashby</title>
<link href="https://fonts.googleapis.com/css2?family=Belleza&family=Cinzel:wght@500&family=Arimo&display=swap" rel="stylesheet">
<style>
  :root {
    --cover-brown: #3e1713;
    --paint-cream: #e6e2d0;
    --paint-sage: #c3c9b4;
    --paint-amber: #d9953f;
    --paint-gold: #efcf7e;
    --paint-rust: #7a3516;
    --title-white: #ffffff;
    --accent-yellow: #f4de7a;
  }
  html, body {
    margin: 0;
    padding: 0;
    overflow: hidden;
    background: var(--cover-brown);
  }
  .cover {
    position: relative;
    width: 858px;
    height: 1200px;
    overflow: hidden;
    background: var(--cover-brown);
  }
  .cover-artwork {
    position: absolute;
    left: 0;
    top: 0;
    width: 858px;
    height: 900px;
    background:
      linear-gradient(180deg,
        var(--paint-cream) 0%,
        var(--paint-sage) 18%,
        var(--paint-gold) 40%,
        var(--paint-amber) 55%,
        var(--paint-rust) 72%,
        var(--cover-brown) 88%);
  }
  .book-title {
    position: absolute;
    left: 164px;
    top: 720px;
    margin: 0;
    font-family: "Belleza", "Optima", sans-serif;
    font-weight: 400;
    font-size: 148px;
    line-height: 138px;
    color: var(--title-white);
    letter-spacing: -2px;
  }
  .book-title .title-line { display: block; }
  .book-title .title-line--second { padding-left: 22px; }
  .trio-mark {
    position: absolute;
    left: 472px;
    top: 1002px;
    width: 44px;
    height: 30px;
  }
  .trio-mark circle {
    fill: none;
    stroke: var(--accent-yellow);
    stroke-width: 1.5;
  }
  .author-name {
    position: absolute;
    right: 133px;
    top: 996px;
    margin: 0;
    padding: 5px 0 4px 6px;
    border-top: 1.5px solid var(--accent-yellow);
    border-bottom: 1.5px solid var(--accent-yellow);
    font-family: "Cinzel", "Trajan Pro", serif;
    font-weight: 500;
    font-size: 26px;
    line-height: 30px;
    color: var(--accent-yellow);
    letter-spacing: 0.5px;
  }
  .series-label {
    position: absolute;
    left: 284px;
    width: 320px;
    top: 1074px;
    margin: 0;
    padding: 8px 0 9px;
    border-top: 1.5px solid var(--accent-yellow);
    border-bottom: 1.5px solid var(--accent-yellow);
    text-align: center;
    font-family: "Arimo", "Arial", sans-serif;
    font-size: 27px;
    line-height: 32px;
    color: var(--title-white);
    letter-spacing: -0.5px;
  }
</style>
</head>
<body>
  <main class="cover">
    <div class="cover-artwork" role="img" aria-label="Painted abstract illustration of figures leaning close together in warm amber, rust and brown tones against a pale sage brushed background"></div>
    <h1 class="book-title">
      <span class="title-line">Falling</span>
      <span class="title-line title-line--second">Softly</span>
    </h1>
    <svg class="trio-mark" viewBox="0 0 44 30" aria-hidden="true">
      <circle cx="13" cy="11" r="9"/>
      <circle cx="31" cy="11" r="9"/>
      <circle cx="22" cy="20" r="9"/>
    </svg>
    <p class="author-name">Maren Ashby</p>
    <p class="series-label">Hartwell Vale Book1</p>
  </main>
</body>
</html>
```